Halvicek Law Group, PLLC
Business card and stationery
Professional
Marcus T. Halvicek, Esq.
President
248 Perrin Avenue
Suite 3407
New York, New York 10093
mhalvicek@halviceklawgroup.example
www.halviceklawgroup.example
Using Ivory-colored card stock
There are 2 additional staff members that need cards:
nothing

```html
<!DOCTYPE html>
<html lang="en">
<head>
<meta charset="utf-8">
<title>Halvicek Law Group, PLLC — Business Card</title>
<link rel="stylesheet" href="https://fonts.googleapis.com/css2?family=Marcellus&family=Open+Sans:ital,wght@0,400;0,600;1,400;1,700&display=swap">
<style>
  :root {
    --backdrop: #3a3a3a;
    --ivory: #fbf9f3;
    --maroon: #6b0f12;
    --maroon-dark: #4a0709;
    --band: #1d1d1d;
    --rule-gray: #9a9a9a;
    --ink-light: #ffffff;
    --brand-ink: #5a1013;
  }
  * { box-sizing: border-box; margin: 0; padding: 0; }
  html, body { width: 1200px; height: 780px; overflow: hidden; }
  body {
    background: var(--backdrop);
    font-family: "Open Sans", Arial, sans-serif;
    position: relative;
  }
  .card {
    position: absolute;
    left: 100px; top: 100px;
    width: 1000px; height: 580px;
    border-radius: 40px;
    overflow: hidden;
    background: var(--ivory);
    box-shadow: 0 10px 30px rgba(0,0,0,0.45);
  }
  .card-shape { position: absolute; inset: 0; }
  .brand-name {
    position: absolute;
    top: 120px; left: 0; right: 0;
    text-align: center;
    font-family: "Marcellus", Georgia, serif;
    font-size: 56px;
    letter-spacing: 3px;
    color: var(--brand-ink);
  }
  .holder {
    position: absolute;
    top: 375px; right: 530px;
    text-align: right;
    color: var(--ink-light);
  }
  .holder-name { font-size: 31px; font-weight: 700; font-style: italic; }
  .holder-title { font-size: 21px; font-style: italic; margin-top: 2px; }
  .holder-address { font-size: 22px; line-height: 1.4; margin-top: 26px; }
  .divider {
    position: absolute;
    left: 500px; top: 360px;
    width: 2px; height: 185px;
    background: rgba(255,255,255,0.7);
  }
  .contact {
    position: absolute;
    left: 520px; top: 352px;
    list-style: none;
    color: var(--ink-light);
    font-size: 21px;
  }
  .contact li { display: flex; align-items: center; height: 44px; }
  .contact svg { width: 22px; height: 22px; margin-right: 14px; flex: none; }
</style>
</head>
<body>
  <div class="card">
    <svg class="card-shape" viewBox="0 0 1000 580" preserveAspectRatio="none" aria-hidden="true">
      <path d="M0,318 C260,290 560,345 1000,248 L1000,580 L0,580 Z" fill="var(--maroon)"/>
      <path d="M0,318 C260,290 560,345 1000,248 L1000,262 C560,358 260,305 0,332 Z" fill="var(--maroon-dark)"/>
      <path d="M0,300 C260,272 560,328 1000,230 L1000,248 C560,345 260,290 0,318 Z" fill="var(--band)"/>
      <path d="M0,290 C260,262 560,318 1000,220" fill="none" stroke="var(--rule-gray)" stroke-width="3"/>
    </svg>

    <div class="brand-name">Halvicek Law Group, PLLC</div>

    <div class="holder">
      <p class="holder-name">Marcus T. Halvicek, Esq.</p>
      <p class="holder-title">President</p>
      <p class="holder-address">248 Perrin Avenue, Suite 3407<br>New York, New York 10093</p>
    </div>

    <div class="divider"></div>

    <ul class="contact">
      <li>
        <svg viewBox="0 0 24 24" aria-label="Phone"><path fill="#fff" d="M6.6 10.8a15 15 0 0 0 6.6 6.6l2.2-2.2c.3-.3.7-.4 1-.2 1.1.4 2.3.6 3.6.6.6 0 1 .4 1 1V20c0 .6-.4 1-1 1A17 17 0 0 1 3 4c0-.6.4-1 1-1h3.5c.6 0 1 .4 1 1 0 1.3.2 2.5.6 3.6.1.3 0 .7-.2 1z"/></svg>
        212-555-0148
      </li>
      <li>
        <svg viewBox="0 0 24 24" aria-label="Fax"><path fill="#fff" d="M7 3h10v5H7zM4 9h16a2 2 0 0 1 2 2v6h-4v4H6v-4H2v-6a2 2 0 0 1 2-2zm4 7v3h8v-3z"/></svg>
        212-555-0173
      </li>
      <li>
        <svg viewBox="0 0 24 24" aria-label="Email"><text x="12" y="19" text-anchor="middle" font-size="22" font-weight="700" fill="#fff" font-family="Arial, sans-serif">@</text></svg>
        mhalvicek@halviceklawgroup.example
      </li>
      <li>
        <svg viewBox="0 0 24 24" aria-label="Website"><g fill="none" stroke="#fff" stroke-width="1.8"><circle cx="12" cy="12" r="9"/><ellipse cx="12" cy="12" rx="4" ry="9"/><path d="M3 12h18M5 7h14M5 17h14"/></g></svg>
        www.halviceklawgroup.example
      </li>
    </ul>
  </div>
</body>
</html>
```